Need a professional looking Consulting site for Consulting Services Company

Stock professional office images with a registration page for contact

Coding

Coded - Design and coding required

```html
<!DOCTYPE html>
<html lang="en">
<head>
<meta charset="utf-8">
<title>Larkfield — Strategy and Growth Advisory</title>
<link rel="stylesheet" href="https://fonts.googleapis.com/css2?family=Montserrat:wght@400;500;600;700&family=Roboto:ital,wght@0,400;0,500;0,700;1,400&display=swap">
<style>
:root{
  --green:#3c9b40;
  --green-bright:#46ad4b;
  --green-dark:#2f8434;
  --ink:#1d1d1d;
  --body:#555;
  --white:#fff;
}
*{box-sizing:border-box;margin:0;padding:0}
html,body{width:1200px;height:5106px;overflow:hidden}
body{position:relative;font-family:"Roboto",sans-serif;color:var(--body);background:var(--white)}
.abs{position:absolute}
.section-title{position:absolute;left:0;width:1200px;text-align:center;font-family:"Montserrat",sans-serif;font-size:42px;font-weight:500;color:var(--ink)}
.section-title::after{content:"";display:block;width:74px;height:4px;background:var(--green);margin:14px auto 0}

/* wordmark: one font, one weight, one colour */
.wordmark{font-family:"Roboto",sans-serif;font-weight:500;line-height:1;white-space:nowrap}

/* hero */
.hero{position:absolute;left:0;top:0;width:1200px;height:688px;background:linear-gradient(160deg,#5d6b73 0%,#3b4850 40%,#2a3238 70%,#4a4f52 100%)}
.hero-photo{position:absolute;inset:0;background:radial-gradient(ellipse at 60% 40%,rgba(210,200,190,.35),transparent 60%)}
.topbar{position:absolute;right:0;top:0;width:640px;height:44px;background:var(--green);clip-path:polygon(30px 0,100% 0,100% 100%,0 100%)}
.topbar-item{position:absolute;top:10px;display:flex;align-items:center;gap:10px;color:#fff;font-size:14px;white-space:nowrap}
.dot-icon{width:24px;height:24px;border-radius:50%;background:#fff;display:flex;align-items:center;justify-content:center}
.social-row{position:absolute;display:flex;gap:6px}
.social-row span{width:24px;height:24px;border:1.5px solid #fff;border-radius:50%}
.header-brand{position:absolute;left:100px;top:22px;font-size:44px;color:#fff}
.nav{position:absolute;top:66px;left:567px;font-family:"Montserrat",sans-serif;font-size:15px;font-weight:500}
.nav a{color:#fff;text-decoration:none;position:absolute;white-space:nowrap}
.nav a.active{color:var(--green-bright)}
.hero-title{position:absolute;top:380px;width:1200px;text-align:center;font-size:90px;color:#fff}
.hero-sub{position:absolute;top:478px;width:1200px;text-align:center;font-size:21px;color:#fff}
.btn{display:inline-block;font-family:"Montserrat",sans-serif;font-weight:600;text-transform:uppercase;text-align:center;text-decoration:none}
.btn-solid{background:var(--green-bright);color:#fff;border-radius:30px}
.btn-line{border:2px solid var(--green);color:var(--green);border-radius:30px;background:#fff}
.hero-btn{position:absolute;left:510px;top:527px;width:180px;height:44px;line-height:44px;font-size:15px}
.dots{position:absolute;top:649px;left:560px;display:flex;gap:12px}
.dots span{width:12px;height:12px;border:1.5px solid #fff;border-radius:50%}
.dots span.on{background:#fff}

/* welcome */
.welcome-photo{position:absolute;left:0;top:688px;width:600px;height:574px;background:linear-gradient(135deg,#8a9aa2,#c9cfd1 45%,#6f7a80 100%)}
.welcome-kicker{position:absolute;left:652px;top:776px;color:var(--green);font-family:"Montserrat",sans-serif;font-weight:600;font-size:24px}
.welcome-title{position:absolute;left:652px;top:804px;font-size:48px;color:var(--ink)}
.rule{position:absolute;height:4px;background:var(--green)}
.welcome-copy{position:absolute;left:652px;top:880px;width:448px;font-size:13.2px;line-height:24.5px;color:var(--body)}
.welcome-copy p+p{margin-top:16px}
.welcome-btn{position:absolute;left:652px;top:1126px;width:174px;height:42px;line-height:38px;font-size:14px}

/* services */
.service{position:absolute;top:1442px;width:317px;height:398px;background:#fff;box-shadow:0 0 12px rgba(0,0,0,.08)}
.service-photo{height:198px;background:linear-gradient(135deg,#c8ced1,#8e9aa0)}
.service-badge{position:absolute;left:128px;top:164px;width:62px;height:62px;border-radius:50%;background:var(--green);border:4px solid #fff;display:flex;align-items:center;justify-content:center}
.service h3{position:absolute;top:248px;width:100%;text-align:center;font-weight:400;font-size:21px;color:var(--ink)}
.service p{position:absolute;top:284px;left:16px;right:16px;text-align:center;font-size:12.5px;line-height:23px}
.service a{position:absolute;top:358px;width:100%;text-align:center;color:var(--green);font-size:13px;font-weight:500;text-decoration:underline}

/* why */
.why{position:absolute;left:0;top:1934px;width:1200px;height:937px;background:linear-gradient(120deg,#eeefee,#f6f6f6 50%,#e9ebea)}
.why-sub{position:absolute;top:2086px;left:220px;width:760px;text-align:center;font-size:17px;line-height:25px;color:var(--ink);font-weight:500}
.why-card{position:absolute;width:448px;height:258px;background:#fff;box-shadow:0 0 10px rgba(0,0,0,.05)}
.why-card .icon{position:absolute;left:22px;top:80px;width:100px;height:100px}
.why-card h4{position:absolute;left:164px;top:38px;font-weight:500;font-size:16px;color:var(--ink)}
.why-card p{position:absolute;left:164px;top:68px;width:250px;font-size:12.3px;line-height:22.5px}
.why-card a{position:absolute;left:164px;top:210px;color:var(--green);font-size:12.5px;font-weight:500;text-decoration:none}

/* testimonials */
.testi{position:absolute;left:0;top:2871px;width:1200px;height:599px;background:linear-gradient(90deg,#3a9a3e,#4ea652 50%,#3a963e)}
.testi-title{color:#fff}
.testi-title::after{background:#fff}
.testi-card{position:absolute;top:3046px;width:436px;height:270px;background:#fff}
.testi-card::after{content:"";position:absolute;left:72px;bottom:-20px;border-right:26px solid transparent;border-top:20px solid #fff}
.avatar{position:absolute;left:24px;top:28px;width:104px;height:104px;border-radius:50%;background:linear-gradient(160deg,#b6bfc4,#5b6870);border:3px solid #e9e9e9}
.quote-mark{position:absolute;left:52px;top:150px}
.testi-card p{position:absolute;left:150px;top:30px;width:262px;font-style:italic;font-size:13.4px;line-height:22.5px;color:var(--body)}
.testi-meta{position:absolute;color:#fff}
.testi-meta .stars{font-size:15px;letter-spacing:1px}
.testi-meta em{display:block;font-size:13px;margin-top:2px}
.testi-meta b{display:block;font-size:13.5px;font-weight:500;margin-top:2px}
.arrow{position:absolute;top:3150px;width:32px;height:32px;border:1.5px solid #fff;border-radius:50%}

/* news */
.news{position:absolute;top:3661px;width:286px}
.news-photo{height:180px;background:linear-gradient(135deg,#6d7377,#c3c7c9 60%,#3f4549)}
.news-body{margin-left:20px;border-left:2px solid var(--green);padding:22px 0 0 26px;height:220px;position:relative}
.news-body h5{font-weight:500;font-size:13.5px;line-height:21px;color:var(--ink);text-transform:uppercase}
.news-date{display:flex;align-items:center;gap:7px;margin-top:12px;font-size:13.5px;color:var(--green)}
.news-body p{margin-top:10px;font-size:12.8px;line-height:22px}
.news-btn{position:absolute;left:26px;top:182px;width:120px;height:26px;line-height:26px;font-size:11px}

/* cta */
.cta{position:absolute;left:0;top:4164px;width:1200px;height:488px;background:linear-gradient(180deg,#3a3f44,#24292d 60%,#1f2225)}
.cta-title{position:absolute;top:4356px;width:1200px;text-align:center;font-size:58px;color:#fff}
.cta-copy{position:absolute;top:4424px;left:320px;width:560px;text-align:center;color:#fff;font-size:18px;line-height:31px}
.cta-btn{position:absolute;left:500px;top:4495px;width:200px;height:40px;line-height:40px;font-size:13px}

/* footer */
.footer{position:absolute;left:0;top:4652px;width:1200px;height:454px;background:var(--green)}
.foot-h{position:absolute;top:4718px;font-weight:700;font-size:22px;color:#fff;text-transform:uppercase}
.foot-contact{position:absolute;left:141px;top:4772px;color:#fff;font-size:13.5px;line-height:23px;width:290px}
.foot-contact .row{display:flex;gap:14px;align-items:flex-start;margin-bottom:10px}
.foot-contact svg{flex:none;margin-top:4px}
.field{position:absolute;left:460px;width:359px;border:1px solid rgba(255,255,255,.75);color:#fff;font-size:11px;padding:10px 12px}
.submit{position:absolute;left:460px;top:4942px;width:158px;height:38px;line-height:34px;border:2px solid #fff;border-radius:24px;color:#fff;font-size:14px}
.quick{position:absolute;left:902px;top:4775px;list-style:none;color:#fff;font-size:13.5px;line-height:27.5px}
.foot-rule{position:absolute;left:0;top:5020px;width:1200px;height:1px;background:rgba(255,255,255,.25)}
.foot-brand{position:absolute;left:141px;top:5044px;font-size:36px;color:#fff}
.copyright{position:absolute;left:475px;top:5053px;color:#fff;font-size:12.5px}
.foot-social{position:absolute;left:873px;top:5044px;display:flex;gap:12px}
.foot-social span{width:38px;height:38px;border:1.5px solid #fff;border-radius:50%}
</style>
</head>
<body>

<header class="hero">
  <div class="hero-photo" role="img" aria-label="Photo of a consulting team gathered around a laptop in a bright office"></div>
  <div class="topbar"></div>
  <div class="topbar-item" style="left:596px">
    <span class="dot-icon"><svg width="13" height="13" viewBox="0 0 24 24"><path fill="#3c9b40" d="M6.6 10.8a15 15 0 0 0 6.6 6.6l2.2-2.2c.3-.3.7-.4 1-.2 1.1.4 2.3.6 3.6.6.6 0 1 .4 1 1V20c0 .6-.4 1-1 1A17 17 0 0 1 3 4c0-.6.4-1 1-1h3.5c.6 0 1 .4 1 1 0 1.3.2 2.5.6 3.6.1.3 0 .7-.2 1z"/></svg></span>
    CALL (555) 014-2290
  </div>
  <div class="topbar-item" style="left:808px">
    <span class="dot-icon"><svg width="13" height="11" viewBox="0 0 24 18"><rect x="1" y="1" width="22" height="16" rx="2" fill="#3c9b40"/><path d="M2 2l10 8 10-8" stroke="#fff" stroke-width="2" fill="none"/></svg></span>
    hello@larkfield.co
  </div>
  <div class="social-row" style="left:1008px;top:9px"><span></span><span></span><span></span></div>

  <div class="header-brand wordmark">Larkfield</div>

  <nav class="nav">
    <a class="active" style="left:0">HOME</a>
    <a style="left:101px">ABOUT</a>
    <a style="left:208px">SERVICES</a>
    <a style="left:339px">BLOG</a>
    <a style="left:434px">CONTACT US</a>
  </nav>

  <h1 class="hero-title wordmark">Larkfield</h1>
  <div class="hero-sub">Strategy and Growth Advisory for Every Stage</div>
  <a class="btn btn-solid hero-btn">Get Started</a>
  <div class="dots"><span></span><span class="on"></span><span></span><span></span></div>
</header>

<section>
  <div class="welcome-photo" role="img" aria-label="Photo of colleagues discussing plans at a meeting table"></div>
  <div class="welcome-kicker">WELCOME TO</div>
  <div class="welcome-title wordmark">Larkfield</div>
  <div class="rule" style="left:652px;top:858px;width:176px"></div>
  <div class="welcome-copy">
    <p>Lorem ipsum dolor sit amet, consectetlit, r incididunt ut labore et dolore magna aliqua. ad minim veniquis nitation ullamco laboris nisi ut aliquip ex ea commodo consequat. Duis aute irure dolorLorem ipsum dolor sit amet, consectetlit, sed do eid tempor</p>
    <p>Sed ut perspiciatis unde omnis is error sit voluptatem accusantium doloremque laudantium, totam rem aperipsa quae ab illo inventore veritatis et quasi architecto beatae vitae dta sunt explicabo. Nemo enim ipsam voluptatem quia voluptas aspernatur aut odit aut fugit, sed quia consequuntur Sed atis unde omnis</p>
  </div>
  <a class="btn btn-line welcome-btn">Learn More</a>
</section>

<section>
  <h2 class="section-title" style="top:1346px">what we do</h2>

  <article class="service" style="left:99px">
    <div class="service-photo" role="img" aria-label="Photo of two consultants reviewing work at a desktop computer"></div>
    <div class="service-badge"><svg width="30" height="30" viewBox="0 0 30 30"><circle cx="15" cy="15" r="11" fill="none" stroke="#fff" stroke-width="2"/><path d="M15 8v14M9 15h12" stroke="#fff" stroke-width="2"/></svg></div>
    <h3>Finibus Bonorum</h3>
    <p>Lorem ipsum dolor sit amet, consectetur adscing elit, sed do eiusmod tempor incunt&nbsp; dolore magna aliq uaLorem ipsum dolor sit</p>
    <a>LEARN MORE »</a>
  </article>

  <article class="service" style="left:441px">
    <div class="service-photo" role="img" aria-label="Photo of a hand holding a pen over financial charts"></div>
    <div class="service-badge"><svg width="30" height="30" viewBox="0 0 30 30"><circle cx="15" cy="15" r="11" fill="none" stroke="#fff" stroke-width="2"/><path d="M15 8v14M9 15h12" stroke="#fff" stroke-width="2"/></svg></div>
    <h3>Finibus Bonorum</h3>
    <p>Lorem ipsum dolor sit amet, consectetur adscing elit, sed do eiusmod tempor incunt&nbsp; dolore magna aliq uaLorem ipsum dolor sit</p>
    <a>LEARN MORE »</a>
  </article>

  <article class="service" style="left:783px">
    <div class="service-photo" role="img" aria-label="Photo of a team working together around a tablet"></div>
    <div class="service-badge"><svg width="30" height="30" viewBox="0 0 30 30"><circle cx="15" cy="15" r="11" fill="none" stroke="#fff" stroke-width="2"/><path d="M15 8v14M9 15h12" stroke="#fff" stroke-width="2"/></svg></div>
    <h3>Finibus Bonorum</h3>
    <p>Lorem ipsum dolor sit amet, consectetur adscing elit, sed do eiusmod tempor incunt&nbsp; dolore magna aliq uaLorem ipsum dolor sit</p>
    <a>LEARN MORE »</a>
  </article>
</section>

<section>
  <div class="why" role="img" aria-label="Faded office background photo"></div>
  <h2 class="section-title" style="top:1999px">why choose us?</h2>
  <div class="why-sub">Sed ut perspiciatis unde omnis iste natus error sit voluptatem accusantium doloremque laudantium, totam rem aperiam, eaque ipsa</div>

  <article class="why-card" style="left:143px;top:2187px">
    <svg class="icon" viewBox="0 0 100 100" fill="none" stroke="#3c9b40" stroke-width="3"><rect x="18" y="20" width="50" height="36"/><path d="M26 48v-8M36 48V34M46 48V28M56 48V38M30 56l-8 26M56 56l8 26M43 56v26"/><circle cx="80" cy="36" r="6"/><path d="M80 44v22M72 82l8-16 8 16M70 52h20"/></svg>
    <h4>FINIBUS BONORUM ET</h4>
    <p>Sed ut pernis e natus error sit voluptatem acntium doloremque laudantium, totam rem aperiam, eaqsa quae ab illo inventore veritatis et quasi architecto beatae vitae dicta sunt explicabo. Nemo enim ipsam voluptatem quia voluptas</p>
    <a>READ MORE &nbsp;»</a>
  </article>

  <article class="why-card" style="left:607px;top:2211px">
    <svg class="icon" viewBox="0 0 100 100" fill="none" stroke="#3c9b40" stroke-width="3"><rect x="36" y="14" width="28" height="18" rx="2"/><path d="M46 32l4 6 4-6"/><circle cx="50" cy="50" r="7"/><path d="M36 76v-10q14-10 28 0v10M20 76h60v8H20zM28 84v6M72 84v6"/></svg>
    <h4>FINIBUS BONORUM ET</h4>
    <p>Sed ut pernis e natus error sit voluptatem acntium doloremque laudantium, totam rem aperiam, eaqsa quae ab illo inventore veritatis et quasi architecto beatae vitae dicta sunt explicabo. Nemo enim ipsam voluptatem quia voluptas</p>
    <a>READ MORE &nbsp;»</a>
  </article>

  <article class="why-card" style="left:143px;top:2463px">
    <svg class="icon" viewBox="0 0 100 100" fill="none" stroke="#3c9b40" stroke-width="3"><circle cx="50" cy="50" r="34"/><path d="M50 16v34h34M50 50L26 74"/><path d="M32 42V30M40 42V24"/><circle cx="72" cy="68" r="10"/><path d="M72 62v12"/></svg>
    <h4>FINIBUS BONORUM ET</h4>
    <p>Sed ut pernis e natus error sit voluptatem acntium doloremque laudantium, totam rem aperiam, eaqsa quae ab illo inventore veritatis et quasi architecto beatae vitae dicta sunt explicabo. Nemo enim ipsam voluptatem quia voluptas</p>
    <a>READ MORE &nbsp;»</a>
  </article>

  <article class="why-card" style="left:607px;top:2487px">
    <svg class="icon" viewBox="0 0 100 100" fill="none" stroke="#3c9b40" stroke-width="3"><path d="M26 14h38l12 12v60H26z"/><path d="M64 14v12h12M34 36h32M34 46h32M34 56h24M34 66h20"/><path d="M58 80l22-22 5 5-22 22-7 2z"/></svg>
    <h4>FINIBUS BONORUM ET</h4>
    <p>Sed ut pernis e natus error sit voluptatem acntium doloremque laudantium, totam rem aperiam, eaqsa quae ab illo inventore veritatis et quasi architecto beatae vitae dicta sunt explicabo. Nemo enim ipsam voluptatem quia voluptas</p>
    <a>READ MORE &nbsp;»</a>
  </article>
</section>

<section>
  <div class="testi" role="img" aria-label="Green tinted photo of an office team"></div>
  <h2 class="section-title testi-title" style="top:2920px">testimonials</h2>

  <svg class="arrow" style="left:84px" viewBox="0 0 32 32"><path d="M18 10l-6 6 6 6" stroke="#fff" stroke-width="2" fill="none"/></svg>
  <svg class="arrow" style="left:1084px" viewBox="0 0 32 32"><path d="M14 10l6 6-6 6" stroke="#fff" stroke-width="2" fill="none"/></svg>

  <article class="testi-card" style="left:153px">
    <div class="avatar" role="img" aria-label="Client portrait"></div>
    <svg class="quote-mark" width="40" height="30" viewBox="0 0 40 30"><path fill="#3c9b40" d="M2 16a10 10 0 1 1 12 9l-6 5 2-6A10 10 0 0 1 2 16zM22 16a10 10 0 1 1 12 9l-6 5 2-6a10 10 0 0 1-8-8z"/></svg>
    <p>Sed ut perspiciati iste natus error sit voluptateloremque laudantium, totam rem aperiam, eaque ipsa quae ab illo inventore veritatis et quasi architecto beatae vitae dicta sxuplicabo. Nemo enim ipsam voluptatem quia voluptas sit aspernatur aut&nbsp; aut fugit, sed quia consequuntur magni dolores eos qui ratione voluptatem sequi</p>
  </article>
  <div class="testi-meta" style="left:224px;top:3322px"><div class="stars">★★★★★</div><em>Nemo enim ipsam</em><b>Daniel Marsh IT Services</b></div>

  <article class="testi-card" style="left:617px">
    <div class="avatar" role="img" aria-label="Client portrait"></div>
    <svg class="quote-mark" width="40" height="30" viewBox="0 0 40 30"><path fill="#3c9b40" d="M2 16a10 10 0 1 1 12 9l-6 5 2-6A10 10 0 0 1 2 16zM22 16a10 10 0 1 1 12 9l-6 5 2-6a10 10 0 0 1-8-8z"/></svg>
    <p>Sed ut perspiciati iste natus error sit voluptateloremque laudantium, totam rem aperiam, eaque ipsa quae ab illo inventore veritatis et quasi architecto beatae vitae dicta sxuplicabo. Nemo enim ipsam voluptatem quia voluptas sit aspernatur aut&nbsp; aut fugit, sed quia consequuntur magni dolores eos qui ratione voluptatem sequi</p>
  </article>
  <div class="testi-meta" style="left:688px;top:3322px"><div class="stars">★★★★★</div><em>Nemo enim ipsam</em><b>Daniel Marsh IT Services</b></div>
</section>

<section>
  <h2 class="section-title" style="top:3546px">latest news</h2>

  <article class="news" style="left:133px">
    <div class="news-photo" role="img" aria-label="Photo of colleagues reviewing reports on a laptop"></div>
    <div class="news-body">
      <h5>Nemo enim ipsam voluptatem quia voluptas sit</h5>
      <div class="news-date"><svg width="13" height="13" viewBox="0 0 14 14"><rect x="1" y="2" width="12" height="11" fill="none" stroke="#3c9b40" stroke-width="1.5"/><path d="M1 5h12M4 0v3M10 0v3" stroke="#3c9b40" stroke-width="1.5"/></svg>Feb 3, 2020</div>
      <p>Sed ut perspiciatis unde omnis iste natus error sit voluptatem accntium domque laudantium, totam</p>
      <a class="btn btn-solid news-btn">Read More</a>
    </div>
  </article>

  <article class="news" style="left:456px">
    <div class="news-photo" role="img" aria-label="Photo of a busy open-plan office"></div>
    <div class="news-body">
      <h5>Nemo enim ipsam voluptatem quia voluptas sit</h5>
      <div class="news-date"><svg width="13" height="13" viewBox="0 0 14 14"><rect x="1" y="2" width="12" height="11" fill="none" stroke="#3c9b40" stroke-width="1.5"/><path d="M1 5h12M4 0v3M10 0v3" stroke="#3c9b40" stroke-width="1.5"/></svg>Feb 3, 2020</div>
      <p>Sed ut perspiciatis unde omnis iste natus error sit voluptatem accntium domque laudantium, totam</p>
      <a class="btn btn-solid news-btn">Read More</a>
    </div>
  </article>

  <article class="news" style="left:781px">
    <div class="news-photo" role="img" aria-label="Photo of two people discussing documents"></div>
    <div class="news-body">
      <h5>Nemo enim ipsam voluptatem quia voluptas sit</h5>
      <div class="news-date"><svg width="13" height="13" viewBox="0 0 14 14"><rect x="1" y="2" width="12" height="11" fill="none" stroke="#3c9b40" stroke-width="1.5"/><path d="M1 5h12M4 0v3M10 0v3" stroke="#3c9b40" stroke-width="1.5"/></svg>Feb 3, 2020</div>
      <p>Sed ut perspiciatis unde omnis iste natus error sit voluptatem accntium domque laudantium, totam</p>
      <a class="btn btn-solid news-btn">Read More</a>
    </div>
  </article>
</section>

<section>
  <div class="cta" role="img" aria-label="Dark photo of a speaker presenting to a seated audience"></div>
  <svg class="abs" style="left:0;top:4164px" width="1200" height="90" viewBox="0 0 1200 90">
    <path d="M0 0H1200V80L600 0 0 80z" fill="#fff"/>
    <path d="M0 80L600 0 1200 80" stroke="#3c9b40" stroke-width="6" fill="none"/>
  </svg>
  <div class="cta-title wordmark">Larkfield</div>
  <div class="cta-copy">Sed ut perspiciatis unde omnis iste natus or sit voluptatem accusantium doloremque laudantium, totam rem ap</div>
  <a class="btn btn-solid cta-btn">Contact Us</a>
</section>

<footer>
  <div class="footer"></div>
  <div class="foot-h" style="left:141px">Contact Us</div>
  <div class="foot-h" style="left:458px">Request a Quote</div>
  <div class="foot-h" style="left:902px">Quick Links</div>

  <div class="foot-contact">
    <div class="row"><svg width="14" height="18" viewBox="0 0 14 18"><path d="M7 17s6-6.5 6-10.5A6 6 0 0 0 1 6.5C1 10.5 7 17 7 17z" fill="none" stroke="#fff" stroke-width="1.5"/><circle cx="7" cy="6.5" r="2" fill="none" stroke="#fff" stroke-width="1.5"/></svg><div>Larkfield<br>48 Fieldstone Avenue Springvale<br>40210</div></div>
    <div class="row"><svg width="16" height="16" viewBox="0 0 24 24"><path fill="none" stroke="#fff" stroke-width="1.8" d="M6.6 10.8a15 15 0 0 0 6.6 6.6l2.2-2.2c.3-.3.7-.4 1-.2 1.1.4 2.3.6 3.6.6.6 0 1 .4 1 1V20c0 .6-.4 1-1 1A17 17 0 0 1 3 4c0-.6.4-1 1-1h3.5c.6 0 1 .4 1 1 0 1.3.2 2.5.6 3.6.1.3 0 .7-.2 1z"/></svg><div>Phone:(555) 014 2290</div></div>
    <div class="row"><svg width="16" height="16" viewBox="0 0 16 16"><rect x="1" y="6" width="14" height="9" fill="#fff"/><rect x="4" y="1" width="8" height="5" fill="none" stroke="#fff" stroke-width="1.5"/></svg><div>Fax: 555 014 2291</div></div>
    <div class="row"><svg width="16" height="12" viewBox="0 0 16 12"><rect x="1" y="1" width="14" height="10" fill="none" stroke="#fff" stroke-width="1.3"/><path d="M1 1l7 6 7-6" fill="none" stroke="#fff" stroke-width="1.3"/></svg><div>Email: hello@larkfield.co</div></div>
  </div>

  <div class="field" style="top:4776px;height:40px">Your Name</div>
  <div class="field" style="top:4826px;height:40px">Email Address</div>
  <div class="field" style="top:4876px;height:58px">Message</div>
  <div class="btn submit">Submit</div>

  <ul class="quick">
    <li>Home</li><li>About</li><li>Services</li><li>Blog</li><li>Contact Us</li>
  </ul>

  <div class="foot-rule"></div>
  <div class="foot-brand wordmark">Larkfield</div>
  <div class="copyright">©Copyright ©2021 Larkfield . All Rights Reserved.</div>
  <div class="foot-social"><span></span><span></span><span></span><span></span></div>
</footer>

</body>
</html>
```